Empowering Stationary for Fitness Business
Iron Harbor: Fitness and Trainings
Empowering Stationary for Fitness Business - Health
Creative Brief
Professional
Ned Farrow
Owner, Certified Personal Trainer
info@ironharborcoaching.example
www.ironharborcoaching.example
I am looking to have the following stationary items created: - business cards - folders - letter head - small note pads - postcard-sized flyer without the stamp area. ( On the front of the flyer please show the full attached logo centered and enlarged with the web address center closer to the bottom of the flyer. On the back please list: - where personal training meets small group trainings - indoor and outdoor weekend sessions - Strength Development - Muscle Stabilization - Functional Movement - Endurance. - team events and outings) - etc., any other examples you care to include Feel free to play around with any ideas.
Highlight the slogan of "Work Out As Hard As You Work" in some way, near the top or bottom of the card. Please use a slightly different font to help it stand out. Please list the following points underneath the slogan with some space between : - where personal training meets small group trainings - indoor and outdoor weekend sessions - group events and outings

```html
<!DOCTYPE html>
<html lang="en">
<head>
<meta charset="utf-8">
<title>Iron Harbor — Business Card</title>
<link href="https://fonts.googleapis.com/css2?family=Marcellus+SC&family=Tenor+Sans&display=swap" rel="stylesheet">
<style>
  :root {
    --backdrop: #c9cacb;
    --card-white: #ffffff;
    --card-charcoal: #3a3a3b;
    --band-charcoal: #3d3d3e;
    --accent-green: #5c8a3c;
    --ink-dark: #4a4a4b;
    --ink-light: #f2f2f2;
    --logo-grey: #6b6b6c;
  }
  html, body {
    margin: 0;
    padding: 0;
    width: 1200px;
    height: 895px;
    overflow: hidden;
    background: var(--backdrop);
  }
  .canvas {
    position: relative;
    width: 1200px;
    height: 895px;
  }
  .card {
    position: absolute;
    width: 560px;
    height: 320px;
    box-shadow: 0 14px 30px rgba(0,0,0,0.28);
    font-family: "Tenor Sans", sans-serif;
    overflow: hidden;
  }

  /* Back of card */
  .card-back {
    left: 580px;
    top: 110px;
    background: var(--card-charcoal);
    color: var(--ink-light);
    text-align: center;
    display: flex;
    flex-direction: column;
    justify-content: center;
    align-items: center;
    gap: 20px;
  }
  .slogan {
    font-family: "Marcellus SC", serif;
    font-size: 22px;
    font-weight: 400;
    letter-spacing: 1px;
    margin: 0 0 6px;
  }
  .service-list {
    list-style: none;
    margin: 0;
    padding: 0 40px;
    display: flex;
    flex-direction: column;
    gap: 14px;
    font-size: 15px;
    letter-spacing: 0.6px;
    line-height: 1.35;
  }

  /* Front of card */
  .card-front {
    left: 60px;
    top: 460px;
    background: var(--card-white);
    color: var(--ink-dark);
  }
  .brand {
    position: absolute;
    top: 62px;
    left: 0;
    right: 0;
    display: flex;
    justify-content: center;
    align-items: center;
    gap: 10px;
  }
  .brand-mark {
    width: 16px;
    height: 16px;
    background: var(--logo-grey);
  }
  .brand-name {
    font-family: "Tenor Sans", sans-serif;
    font-size: 30px;
    letter-spacing: 2px;
    color: var(--logo-grey);
    text-transform: uppercase;
  }
  .band-rule {
    position: absolute;
    left: 0;
    right: 0;
    top: 145px;
    height: 1px;
    background: var(--accent-green);
  }
  .name-band {
    position: absolute;
    left: 0;
    right: 0;
    top: 150px;
    height: 40px;
    background: var(--band-charcoal);
    border-top: 2px solid var(--accent-green);
    border-bottom: 2px solid var(--accent-green);
    color: var(--ink-light);
    display: flex;
    align-items: center;
    padding-left: 34px;
    font-family: "Marcellus SC", serif;
    font-size: 14px;
    letter-spacing: 0.8px;
  }
  .name-band .divider { margin: 0 10px; }
  .contact {
    position: absolute;
    left: 34px;
    top: 212px;
    display: flex;
    flex-direction: column;
    gap: 8px;
    font-size: 13px;
    letter-spacing: 0.6px;
  }
  .contact-row {
    display: flex;
    align-items: center;
    gap: 8px;
  }
  .contact-row svg { width: 14px; height: 14px; flex: none; }
  .contact-row .sep { margin: 0 4px; color: var(--ink-dark); }
</style>
</head>
<body>
<main class="canvas">

  <section class="card card-back" aria-label="Business card back">
    <h2 class="slogan">Work Out As Hard As You Work</h2>
    <ul class="service-list">
      <li>where personal training meets small group trainings</li>
      <li>indoor and outdoor weekend sessions</li>
      <li>Strength Development - Muscle Stabilization -<br>Functional Movement - Endurance.</li>
      <li>team events and outings!</li>
    </ul>
  </section>

  <section class="card card-front" aria-label="Business card front">
    <div class="brand">
      <span class="brand-mark"></span>
      <span class="brand-name">Iron Harbor</span>
    </div>

    <div class="band-rule"></div>
    <div class="name-band">
      <span>Ned Farrow</span><span class="divider">|</span><span>Owner, Certified Personal Trainer</span>
    </div>

    <div class="contact">
      <div class="contact-row">
        <svg viewBox="0 0 14 14" aria-hidden="true">
          <circle cx="7" cy="7" r="7" fill="#4a4a4b"/>
          <path d="M4.4 3.6 l1.4 0 l0.5 1.8 l-0.9 0.7 a5 5 0 0 0 2.5 2.5 l0.7 -0.9 l1.8 0.5 l0 1.4 a1 1 0 0 1 -1 0.9 a6.4 6.4 0 0 1 -5.9 -5.9 a1 1 0 0 1 0.9 -1 z" fill="#ffffff"/>
        </svg>
        <span>555-014-2290</span>
        <span class="sep">|</span>
        <svg viewBox="0 0 14 14" aria-hidden="true">
          <circle cx="7" cy="7" r="7" fill="#4a4a4b"/>
          <rect x="3.5" y="4.5" width="7" height="5" fill="none" stroke="#ffffff" stroke-width="1"/>
          <path d="M3.5 4.5 L7 7.5 L10.5 4.5" fill="none" stroke="#ffffff" stroke-width="1"/>
        </svg>
        <span>info@ironharborcoaching.example</span>
      </div>
      <div class="contact-row">
        <svg viewBox="0 0 14 14" aria-hidden="true">
          <circle cx="7" cy="7" r="7" fill="#4a4a4b"/>
          <circle cx="7" cy="7" r="3.6" fill="none" stroke="#ffffff" stroke-width="0.9"/>
          <path d="M3.4 7 H10.6 M7 3.4 C5.4 5 5.4 9 7 10.6 M7 3.4 C8.6 5 8.6 9 7 10.6" fill="none" stroke="#ffffff" stroke-width="0.8"/>
        </svg>
        <span>www.ironharborcoaching.example</span>
      </div>
    </div>
  </section>

</main>
</body>
</html>
```